People Search Directory Needs a Web Design

We need a web design for a new web site called Kestrel Lineage Lookups. We provide free directory information, such as name, phone, address, and email. We also provide other non-white pages information such as the person's relatives, historical records to help identify the person, and link the data so people can find connections. For example, by clicking on an address that a person lives at, you can find other people who might currently (or previously) have lived at that address.

We have a very basic web page that contains a lot of public records data. The page can look very busy. We need it to be concise, where the white pages type of information is easily identifiable, but people also realize the usefulness of the surrounding data (such as possible relatives, email address, historical phone numbers, etc).

The web page also promotes an annual membership to get more in-depth information on people. These Kestrel Lineage Lookups include a criminal records check, property records, and other information.

Industry/Entity Type

Property

Requirements
Must have
• Attached is an example design we put together. We want the design to be snazzier, have more information architecture thought put into it, etc.

```html
<!DOCTYPE html>
<html lang="en">
<head>
<meta charset="utf-8">
<title>Kestrel Lineage Lookups</title>
<link href="https://fonts.googleapis.com/css2?family=Arimo:wght@400;700&family=Tinos&display=swap" rel="stylesheet">
<style>
:root{
  --ink:#222;
  --text:#666;
  --muted:#888;
  --teal:#5bb3a6;
  --field:#566e8c;
  --orange:#f6a619;
  --link:#c14a09;
  --green:#6fb522;
  --blue-panel:#d3ecef;
  --button-blue:#4a9cd8;
  --footer:#2b2b2b;
}
*{box-sizing:border-box;margin:0;padding:0}
html,body{width:915px;height:1200px;overflow:hidden;background:#fff}
body{position:relative;font-family:"Arimo",Arial,sans-serif;color:var(--text);font-size:10px;line-height:16.6px}
.abs{position:absolute}

.main-nav{left:37px;top:57px;width:236px;height:32px;border:1px solid #ddd;border-top:none;border-left:none;background:linear-gradient(#fff,#f4f4f4);display:flex;align-items:center;gap:4px;padding-left:5px}
.main-nav a{font-size:10.5px;color:#555;text-decoration:none;padding:6px 9px;border-radius:2px}
.main-nav a.active{background:#1e1e1e;color:#fff}

.brand{left:472px;top:55px;display:flex;align-items:center;gap:8px;font-size:18.5px;font-weight:700;letter-spacing:1.6px;color:var(--teal)}
.brand-mark{width:14px;height:14px;background:var(--button-blue)}

.hero{left:36px;top:97px;width:549px;height:266px;background:radial-gradient(ellipse at 55% 35%,#ebe8e5 0%,#b7b0aa 55%,#8f8780 100%)}
.hero-photo{left:585px;top:97px;width:250px;height:266px;background:linear-gradient(180deg,#f3ede6 0%,#d8c4ad 45%,#3a2f2a 100%)}
.arrow{top:210px}
.search-card{left:86px;top:144px;width:461px;height:147px;border-radius:10px;background:linear-gradient(#f7f6f4,#e3e1de);box-shadow:0 2px 6px rgba(0,0,0,.25)}
.search-card h1{position:absolute;left:20px;top:20px;font-family:"Tinos",Georgia,serif;font-weight:400;font-size:22px;letter-spacing:-.8px;color:#2a2f3a}
.field{position:absolute;height:22px;background:var(--field);color:#fff;font-weight:700;font-size:10.5px;line-height:22px;padding-left:7px;border:1px solid #8ea0b8}
.field .caret{position:absolute;right:3px;top:3px;width:14px;height:14px;background:#e9edf2;border-radius:2px}
.search-btn{position:absolute;left:304px;top:84px;width:131px;height:30px;border-radius:3px;background:linear-gradient(#ffd64a,var(--orange));border:1px solid #d48a0c;color:#d9400a;font-weight:700;font-size:16px;text-align:center;line-height:28px}
.search-card .hint{position:absolute;left:24px;top:121px;font-weight:700;font-size:10.5px;color:#555}

.ticker{left:36px;top:329px;width:549px;height:34px;background:rgba(40,35,32,.72);color:#fff;font-size:10px;display:flex;align-items:center;padding-left:14px}
.ticker .rss{width:12px;height:12px;background:#f08a1c;border-radius:2px;margin-right:14px}
.ticker b{font-weight:400;margin-right:11px}
.ticker .more{margin-left:auto;margin-right:9px;background:#fff;color:#666;padding:3px 7px;font-size:10px}

h2{font-weight:400;font-size:17px;color:var(--ink);letter-spacing:-.2px;line-height:20px}
.sub{font-size:8.2px;color:var(--muted);line-height:11px}

.about{left:47px;top:390px;width:450px}
.about p{margin-top:12px}
.quote{position:absolute;left:34px;width:462px;height:78px;border:1px solid #e2e6e6;background:#f7f9f9;font-style:italic;color:#8a8a8a;padding:19px 12px}

.offer{left:35px;top:956px;width:431px;height:142px;border:1px solid #a9d07a}
.offer-icon{left:12px;top:14px;width:52px;height:52px;background:linear-gradient(135deg,#e8ece8,#9fa7a4)}
.offer h3{position:absolute;left:73px;top:15px;font-size:12px;color:var(--ink)}
.offer h3 em{font-style:normal;color:var(--button-blue)}
.offer ul{position:absolute;list-style:none;top:38px;font-size:10.5px;color:#333;line-height:17px}
.offer li{position:relative;padding-left:20px}
.offer li svg{position:absolute;left:0;top:3px}
.green-btn{position:absolute;left:73px;top:101px;width:220px;height:19px;background:linear-gradient(#7cc52d,#5ea219);color:#fff;font-weight:700;font-size:10px;line-height:19px;text-align:center}

.news{left:544px;top:388px;width:280px}
.news-item{position:absolute;left:2px;width:280px}
.thumb{position:absolute;left:0;top:0;width:58px;height:58px;border:1px solid #ddd;padding:3px;background:#fff}
.thumb span{display:block;width:100%;height:100%}
.news-body{position:absolute;left:76px;top:-2px;width:200px;color:#555}
.news-body strong{color:var(--ink);font-size:10px}
.meta{color:var(--link);font-size:9px}
.meta b{color:var(--link)}
.morelink{color:#999;font-weight:700}

.testimonials{left:546px;top:732px;width:280px}
.testi{position:absolute;left:0;width:280px}
.avatar{position:absolute;left:0;top:0;width:46px;height:46px;border:1px solid #ddd;padding:3px}
.avatar span{display:block;width:100%;height:100%;background:linear-gradient(#c9e2ec,#6ea9c4)}
.testi p{position:absolute;left:58px;top:-3px;width:205px;color:#555}
.testi i{font-weight:700;color:#333}

.report{left:544px;top:943px;width:258px;height:107px;background:var(--blue-panel);padding:12px 14px}
.report h3{font-size:12px;color:var(--ink);margin-bottom:2px}
.report p{font-size:10px;line-height:11px;color:#444}
.blue-btn{margin-top:7px;width:191px;height:19px;background:linear-gradient(#6cb6e8,#3d8dcc);color:#fff;font-weight:700;font-size:10px;line-height:19px;text-align:center}

.footer{left:32px;top:1121px;width:816px;height:44px;background:var(--footer);border-radius:2px;color:#ddd;font-size:8.2px;line-height:11px;padding:10px 20px}
</style>
</head>
<body>

<nav class="main-nav abs">
  <a href="#">Home</a>
  <a href="#" class="active">People Directory</a>
  <a href="#">Contact Us</a>
</nav>

<div class="brand abs"><span>KESTREL LINEAGE LOOKUPS</span><span class="brand-mark"></span></div>

<svg class="abs arrow" style="left:7px" width="20" height="40" viewBox="0 0 20 40"><polyline points="17,3 4,20 17,37" fill="none" stroke="#a8a8a8" stroke-width="4"/></svg>
<svg class="abs arrow" style="left:845px" width="20" height="40" viewBox="0 0 20 40"><polyline points="3,3 16,20 3,37" fill="none" stroke="#a8a8a8" stroke-width="4"/></svg>

<div class="hero abs"></div>
<div class="hero-photo abs" role="img" aria-label="Portrait photo of a smiling woman"></div>

<form class="search-card abs">
  <h1>Kestrel Lineage Lookups</h1>
  <div class="field" style="left:23px;top:55px;width:133px">First Name</div>
  <div class="field" style="left:163px;top:55px;width:133px">Last Name</div>
  <div class="field" style="left:304px;top:55px;width:131px">City<span class="caret"></span></div>
  <div class="field" style="left:23px;top:89px;width:272px;font-style:italic">All States<span class="caret"></span></div>
  <div class="search-btn">Search</div>
  <div class="hint">Find your background</div>
</form>

<div class="ticker abs">
  <span class="rss"></span>
  <b>KESTREL LL</b>
  <span>Donec tincidunt, felis sit amet vestibulum scelerisque, sapien nisi cursus nisi</span>
  <span class="more">READ MORE</span>
</div>

<section class="about abs">
  <h2>About Our Company.</h2>
  <div class="sub">Lorem ipsum dolor sit amet, consectetur adipisicing elit, sed do eiusmod tempor</div>
  <p style="margin-top:17px">Sed ut perspiciatis unde omnis iste natus error sit voluptatem accusantium mque laudantium, totam rem aperiam, eaque ipsa quae ab illo inventore veritatis et quasi architecto beatae vitae dicta sunt explicabo ullamco laboris nisi ut aliquip ex ea commodo consequat.</p>
</section>

<div class="quote" style="top:499px">Vestibulum vehicula purus nec dui accumsan fermentum. Suspendisse potenti. Ut dapibus est id odio pretium blandit in eget leo. Aliquam erat volutpat.</div>

<div class="abs" style="left:47px;top:591px;width:440px">
  <p>Lorem ipsum dolor sit amet, consectetur adipisicing elit, sed do eiusmod tempor incididunt ut labore et dolore magna aliqua. Ut enim ad minim veniam, quis nostrud exercitation ullamco laboris nisi ut aliquip exea commodo consequat. Duis aute irure dolor in reprehenderit in voluptate velit esse cillum dolore eu fugiat nulla pariatur.</p>
  <p style="margin-top:15px;line-height:15px">The point of using Lorem Ipsum is that it has a more-or-less normal distribution of letters, as opposed to using 'Content here, content here', making it look like readable English.</p>
  <p style="margin-top:15px;line-height:15px">Many desktop publishing packages and web page editors now use Lorem Ipsum as their default model text, and a search for 'lorem ipsum' will uncover many web sites still in their infancy. Various versions have evolved over the years, sometimes by accident, sometimes on purpose (injected humour and the like).</p>
</div>

<div class="quote" style="top:806px">Vestibulum vehicula purus nec dui accumsan fermentum. Suspendisse potenti. Ut dapibus est id odio pretium blandit in eget leo. Aliquam erat volutpat.</div>

<p class="abs" style="left:49px;top:901px;width:450px">Lorem ipsum dolor sit amet, consectetur adipiscing elit. Quisque a tellus dolor. &nbsp;Etiam vel tortor et elit commodo fringilla. Cras eget consectetur metus. Phasellus varius dignissim risus, id gravida.</p>

<section class="offer abs">
  <div class="offer-icon abs" role="img" aria-label="Illustration of a report document"></div>
  <h3>Want more in-depth information on <em>Marisol T Brennan</em>?</h3>
  <ul style="left:73px">
    <li><svg width="13" height="11" viewBox="0 0 13 11"><polyline points="1,6 5,10 12,1" fill="none" stroke="#6fb522" stroke-width="2.5"/></svg>Name and AKAs</li>
    <li><svg width="13" height="11" viewBox="0 0 13 11"><polyline points="1,6 5,10 12,1" fill="none" stroke="#6fb522" stroke-width="2.5"/></svg>Up to 40-year address history</li>
    <li><svg width="13" height="11" viewBox="0 0 13 11"><polyline points="1,6 5,10 12,1" fill="none" stroke="#6fb522" stroke-width="2.5"/></svg>Date of birth</li>
  </ul>
  <ul style="left:256px">
    <li><svg width="13" height="11" viewBox="0 0 13 11"><polyline points="1,6 5,10 12,1" fill="none" stroke="#6fb522" stroke-width="2.5"/></svg>Evictions &amp; bankruptcies</li>
    <li><svg width="13" height="11" viewBox="0 0 13 11"><polyline points="1,6 5,10 12,1" fill="none" stroke="#6fb522" stroke-width="2.5"/></svg>Property records</li>
    <li><svg width="13" height="11" viewBox="0 0 13 11"><polyline points="1,6 5,10 12,1" fill="none" stroke="#6fb522" stroke-width="2.5"/></svg>Criminal records check</li>
  </ul>
  <div class="green-btn">Get advanced background report...</div>
</section>

<section class="news abs">
  <h2>Latest From the News</h2>
  <div class="sub">Lorem ipsum dolor sit amet, consectetur adipisicing elit</div>
  <div class="news-item" style="top:59px">
    <div class="thumb"><span role="img" aria-label="News thumbnail" style="background:#2e7a2a"></span></div>
    <div class="news-body"><strong>Another News</strong><br><span class="meta">July 28th, 2009 | <b>23 Comments</b></span><br>Mauris ante dui, placerat at malesuada in, suscipit sit amet lectus. <span class="morelink">more »</span></div>
  </div>
  <div class="news-item" style="top:142px">
    <div class="thumb"><span role="img" aria-label="News thumbnail" style="background:#3a3a3a"></span></div>
    <div class="news-body"><strong>Another News</strong><br><span class="meta">July 28th, 2009 | <b>36 Comments</b></span><br>Lorem ipsum dolor sit amet, consectetur adipiscing elit. &nbsp;<span class="morelink">more »</span></div>
  </div>
  <div class="news-item" style="top:225px">
    <div class="thumb"><span role="img" aria-label="News thumbnail" style="background:#e2e2e2"></span></div>
    <div class="news-body"><strong>Another News</strong><br><span class="meta">July 28th, 2009 | <b>45 Comments</b></span><br>Phasellus consectetur, nisi sed placerat at malesuada suscipit ultricies, risus ligula condimentum arcu. <span class="morelink">more »</span></div>
  </div>
</section>

<section class="testimonials abs">
  <h2>What They Say</h2>
  <div class="sub">Lorem ipsum dolor sit amet, consectetur adipiscing elit</div>
  <div class="testi" style="top:61px">
    <div class="avatar"><span role="img" aria-label="Customer avatar"></span></div>
    <p>"Quis autem vel eum iure reprehenderit qui in ea voluptate velit esse voluptas nulla pariatur?" &nbsp;<i>by: Peter L., webdesigner</i></p>
  </div>
  <div class="testi" style="top:133px">
    <div class="avatar"><span role="img" aria-label="Customer avatar"></span></div>
    <p>"Quis autem vel eum iure reprehenderit qui in ea voluptate velit esse voluptas nulla pariatur?" &nbsp;<i>by: Peter L., webdesigner</i></p>
  </div>
</section>

<aside class="report abs">
  <h3>What's in your background report?</h3>
  <p>See what records are publicly available in your background report. Also, check out the public records in reports for your friends and family.</p>
  <div class="blue-btn">Check my background report...</div>
</aside>

<footer class="footer abs">
  © Copyright websitename . All Rights Reserved<br>
  Home | People Directory | Privacy | Terms | Contact Us
</footer>

</body>
</html>
```